Website for a Party Bus charter business

Please prepare a site for a local party bus charter company names Holloway Bus Company.
They hire a party bus, chatrer bus, boat hire and party trailer hire (place holder photos fine for these items).
I have included a wireframe design. This should be used, however creative licence is fully extended
Delivery of PSD is required and all fonts and source files
The client likes: http://www.tallquorin.com.au/ but must not look completely the same.
Should use a gold (simualr to #D1CFA1) colour, even if just background.
Updates
Hi All, just wondering if anyone is working on this as I have not received any responses or questions?
Is there anything I can do to assist?
Thanks all for the great submissions. I will be sending these onto the client today. Will let you know the outcome as soon as I can
Industry/Entity Type
Business
Look and feel
Each slider illustrates characteristics of the customer's brand and the style your logo design should communicate.

```html
<!DOCTYPE html>
<html lang="en">
<head>
<meta charset="utf-8">
<title>Holloway Bus Company</title>
<link rel="stylesheet" href="https://fonts.googleapis.com/css2?family=Bebas+Neue&family=Arimo:wght@400;700&display=swap">
<style>
:root{
  --gold:#d1cfa1;
  --gold-soft:#e4e2c4;
  --blue:#3a4f9b;
  --blue-dark:#2d3f82;
  --ink:#3e3e3e;
  --muted:#8a8a8a;
  --line:#d8d8d8;
  --page:#ffffff;
  --footer:#2e2e2e;
  --footer-text:#bdbdbd;
  --fb:#3b5b9a;
  --tw:#35aee0;
  --gp:#d8452f;
  --mail:#3aa655;
  --photo-a:#8e9aa6;
  --photo-b:#c9ced3;
}
*{box-sizing:border-box;margin:0;padding:0}
html,body{width:1200px;height:2218px;overflow:hidden}
body{position:relative;background:var(--page);font-family:"Arimo",Arial,sans-serif;color:var(--ink);font-size:11px;line-height:1.4}
.abs{position:absolute}
.display{font-family:"Bebas Neue",Impact,sans-serif;letter-spacing:.5px}
.photo{background:linear-gradient(160deg,var(--photo-b),var(--photo-a));}
p.copy{font-size:11px;color:#6d6d6d;line-height:1.35}

/* header */
.site-header{left:0;top:0;width:1200px;height:94px;background:#fff;overflow:hidden}
.header-band{left:0;top:0}
.brand{left:94px;top:16px;display:flex;align-items:center;gap:14px}
.brand-mark{width:60px;height:60px;border-radius:50%;background:var(--blue)}
.brand-name{font-family:"Bebas Neue",Impact,sans-serif;color:var(--blue);font-size:40px;line-height:.85}
.brand-name span{display:block;font-size:22px;letter-spacing:5px;padding-left:70px}
.header-social{left:579px;top:10px;display:flex;gap:8px}
.header-social i{width:28px;height:28px;display:block;border-radius:3px}
.search{left:796px;top:12px;width:190px;height:26px;background:#fff;border:1px solid #cfcfcf;border-radius:3px;padding:5px 8px;color:#aaa;font-size:11px}
.like{left:996px;top:11px;width:68px;height:28px;border:1px solid #b9c2d8;background:#eef0f6;border-radius:3px;font-size:13px;font-weight:700;color:var(--blue);display:flex;align-items:center;justify-content:center;gap:6px}
.like i{width:12px;height:12px;background:var(--blue);display:block}
.contact-row{top:60px;font-size:12px;color:#9a9a9a;display:flex;align-items:center;gap:8px;white-space:nowrap}
.contact-row svg{fill:#b5b5b5}

/* slider */
.slider{left:0;top:94px;width:1200px;height:316px;background:#f4f4f2}
.slide{position:absolute;border:5px solid #fff;box-shadow:0 3px 8px rgba(0,0,0,.3)}
.slide-caption{position:absolute;left:0;right:0;bottom:0;padding:8px 10px;background:rgba(0,0,0,.45);color:#fff;font-size:16px}

/* nav */
.main-nav{left:0;top:411px;width:1200px;height:66px;background:linear-gradient(var(--blue),var(--blue-dark))}
.main-nav ul{list-style:none;display:flex;justify-content:space-between;width:1018px;margin:0 auto;height:66px;align-items:center}
.main-nav li{font-family:"Bebas Neue",Impact,sans-serif;color:#fff;font-size:30px;letter-spacing:.5px;white-space:nowrap}

/* section titles */
.section-title{font-family:"Bebas Neue",Impact,sans-serif;color:var(--blue);font-size:34px;line-height:1;left:91px;width:1018px;border-bottom:1px solid var(--line);padding-bottom:4px}

/* services */
.service{display:flex;gap:16px;width:495px;height:124px}
.service .photo{width:123px;height:118px;border:3px solid #fff;box-shadow:0 1px 4px rgba(0,0,0,.35);flex:none}
.service h3{font-family:"Bebas Neue",Impact,sans-serif;font-weight:400;font-size:26px;color:#555;line-height:1}
.btn{display:inline-flex;align-items:center;justify-content:center;background:var(--blue);color:#fff;font-family:"Bebas Neue",Impact,sans-serif;font-size:14px;letter-spacing:.5px;height:28px;padding:0 14px;white-space:nowrap;line-height:1}
.service .btn{position:absolute;right:0;bottom:4px;width:88px}
.service-body{position:relative;flex:1}

/* video */
.video-band{left:0;top:838px;width:1200px;height:443px;background:var(--gold)}
.video{left:91px;top:862px;width:1018px;height:400px;background:linear-gradient(135deg,#3f4548,#1c2022 55%,#2c3236)}

/* coast */
.coast-photo{left:91px;top:1357px;width:500px;height:330px;border:6px solid #fff;box-shadow:0 3px 10px rgba(0,0,0,.35)}
.coast-text{left:611px;top:1352px;width:498px}
.coast-text p{margin-bottom:12px;text-align:justify}

/* social */
.feed{width:318px}
.feed-head{height:38px;border:2px solid;display:flex;align-items:center;justify-content:space-between;padding:0 6px 0 8px;font-family:"Bebas Neue",Impact,sans-serif;font-size:18px;white-space:nowrap}
.feed-head i{width:26px;height:26px;display:block}
.post{display:flex;gap:10px;margin-top:12px;height:62px}
.post .avatar{width:62px;height:50px;flex:none;background:var(--line);border-radius:4px}
.post p{font-size:10px;color:#777;line-height:1.3}

/* footer */
.footer{left:0;top:1971px;width:1200px;height:202px;background:var(--footer);color:var(--footer-text)}
.footer h4{font-family:"Bebas Neue",Impact,sans-serif;font-weight:400;color:#fff;font-size:30px;line-height:1;border-bottom:1px solid #555;padding-bottom:4px}
.footer p{font-size:10.5px;color:var(--footer-text);line-height:1.35}
.footer .post{height:58px;margin-top:10px}
.field{height:28px;background:#fff;border:1px solid #ccc;color:#555;font-size:12px;padding:6px 8px}
.bottom-bar{left:0;top:2173px;width:1200px;height:45px;background:#fff}
</style>
</head>
<body>

<header class="abs site-header">
  <svg class="abs header-band" width="1200" height="94" viewBox="0 0 1200 94">
    <path d="M430 0 H1200 V42 H700 C560 42 520 6 430 0 Z" fill="var(--gold)"/>
    <path d="M0 86 H1200" stroke="#ececec" stroke-width="2"/>
  </svg>
  <div class="abs brand">
    <div class="brand-mark"></div>
    <div class="brand-name">Holloway Bus<span>Company</span></div>
  </div>
  <div class="abs header-social">
    <i style="background:var(--fb)"></i><i style="background:var(--tw)"></i><i style="background:var(--gp)"></i><i style="background:var(--mail)"></i>
  </div>
  <div class="abs search">Search</div>
  <div class="abs like"><i></i>Like</div>
  <div class="abs contact-row" style="left:545px">
    <svg width="20" height="16" viewBox="0 0 20 16"><path d="M10 1 L19 8 H16 V15 H4 V8 H1 Z"/></svg>Complete Adress
  </div>
  <div class="abs contact-row" style="left:718px">
    <svg width="20" height="14" viewBox="0 0 20 14"><rect width="20" height="14" rx="2"/><path d="M1 1 L10 8 L19 1" stroke="#fff" fill="none"/></svg>contact@hollowaybuscompany.com
  </div>
  <div class="abs contact-row" style="left:988px">
    <svg width="18" height="16" viewBox="0 0 18 16"><path d="M2 2 C2 10 8 15 16 15 L17 11 L13 9 L11 11 C8 10 6 8 5 5 L7 3 L5 0 Z"/></svg>123.456.7890
  </div>
</header>

<section class="abs slider" aria-label="Fleet slider">
  <div class="slide photo" role="img" aria-label="Bus at a stop" style="left:99px;top:54px;width:50px;height:195px"></div>
  <div class="slide photo" role="img" aria-label="Bus parked by a building" style="left:153px;top:36px;width:78px;height:228px"></div>
  <div class="slide photo" role="img" aria-label="Bus in town street" style="left:234px;top:20px;width:150px;height:262px"></div>
  <div class="slide photo" role="img" aria-label="City bus at a bus stop" style="left:385px;top:16px;width:414px;height:288px">
    <div class="slide-caption">Lorem ipsum at nue keverski at nower test.</div>
  </div>
  <div class="slide photo" role="img" aria-label="Bus on a road" style="left:800px;top:22px;width:158px;height:258px"></div>
  <div class="slide photo" role="img" aria-label="Bus at depot" style="left:961px;top:38px;width:76px;height:222px"></div>
  <div class="slide photo" role="img" aria-label="Bus side view" style="left:1040px;top:54px;width:62px;height:192px"></div>
</section>

<nav class="abs main-nav">
  <ul>
    <li>Home</li><li>Party Bus</li><li>Charter Bus</li><li>Party Trailer</li><li>Party Boat</li><li>House Bus</li><li>What You Own?</li><li>Contact</li>
  </ul>
</nav>

<h2 class="abs section-title" style="top:496px">Holloway Bus Company</h2>

<article class="abs service" style="left:94px;top:548px">
  <div class="photo" role="img" aria-label="Party bus"></div>
  <div class="service-body">
    <h3>Lorem Ipsum</h3>
    <p class="copy">Lorem ipsum dolor sit amet, consectetur adipiscing elit, sed do eiusmod tempor incididunt ut labore et dolore magna aliqua. Ut enim ad minim veniam, quis nostrud exercitation ullamco laboris nisi ut aliquip ex ea commodo consequat.</p>
    <span class="btn">More</span>
  </div>
</article>
<article class="abs service" style="left:614px;top:548px">
  <div class="photo" role="img" aria-label="Charter bus"></div>
  <div class="service-body">
    <h3>Lorem Ipsum</h3>
    <p class="copy">Lorem ipsum dolor sit amet, consectetur adipiscing elit, sed do eiusmod tempor incididunt ut labore et dolore magna aliqua. Ut enim ad minim veniam, quis nostrud exercitation ullamco laboris nisi ut aliquip ex ea commodo consequat.</p>
    <span class="btn">More</span>
  </div>
</article>
<article class="abs service" style="left:94px;top:696px">
  <div class="photo" role="img" aria-label="Party trailer"></div>
  <div class="service-body">
    <h3>Lorem Ipsum</h3>
    <p class="copy">Lorem ipsum dolor sit amet, consectetur adipiscing elit, sed do eiusmod tempor incididunt ut labore et dolore magna aliqua. Ut enim ad minim veniam, quis nostrud exercitation ullamco laboris nisi ut aliquip ex ea commodo consequat.</p>
    <span class="btn">More</span>
  </div>
</article>
<article class="abs service" style="left:614px;top:696px">
  <div class="photo" role="img" aria-label="Party boat"></div>
  <div class="service-body">
    <h3>Lorem Ipsum</h3>
    <p class="copy">Lorem ipsum dolor sit amet, consectetur adipiscing elit, sed do eiusmod tempor incididunt ut labore et dolore magna aliqua. Ut enim ad minim veniam, quis nostrud exercitation ullamco laboris nisi ut aliquip ex ea commodo consequat.</p>
    <span class="btn">More</span>
  </div>
</article>

<section class="abs video-band">
</section>
<div class="abs video" role="img" aria-label="Video still of a city bus at night">
  <svg class="abs" style="left:469px;top:160px" width="80" height="80" viewBox="0 0 80 80"><path d="M18 8 L70 40 L18 72 Z" fill="#fff"/></svg>
</div>

<h2 class="abs section-title" style="top:1306px">Best Way to See the Coast</h2>
<div class="abs coast-photo photo" role="img" aria-label="White bus parked on a street"></div>
<div class="abs coast-text">
  <p class="copy">Lorem ipsum dolor sit amet, consectetur adipiscing elit, sed do eiusmod tempor incididunt ut labore et dolore magna aliqua. Ut enim ad minim veniam, quis nostrud exercitation ullamco laboris nisi ut aliquip ex ea commodo consequat.</p>
  <p class="copy">Lorem ipsum dolor sit amet, consectetur adipiscing elit, sed do eiusmod tempor incididunt ut labore et dolore magna aliqua. Ut enim ad minim veniam, quis nostrud exercitation ullamco laboris nisi ut aliquip ex ea commodo consequat. Duis aute irure dolor in reprehenderit in voluptate velit esse cillum dolore eu fugiat nulla pariatur. Excepteur sint occaecat cupidatat non proident, sunt in culpa qui officia deserunt mollit anim id est laborum.</p>
  <p class="copy">Sed ut perspiciatis unde omnis iste natus error sit voluptatem accusantium doloremque laudantium, totam rem aperiam, eaque ipsa quae ab illo inventore veritatis et quasi architecto beatae vitae dicta sunt explicabo. Nemo enim ipsam voluptatem quia voluptas sit aspernatur aut odit aut fugit, sed quia consequuntur magni dolores eos qui ratione voluptatem sequi nesciunt. Neque porro quisquam est, qui dolorem ipsum quia dolor sit amet, consectetur, adipisci velit.</p>
</div>
<span class="abs btn" style="left:1023px;top:1662px;height:28px;width:86px;padding:0">Book It Now</span>

<h2 class="abs section-title" style="top:1720px">Social Feed</h2>

<div class="abs feed" style="left:91px;top:1774px">
  <div class="feed-head" style="border-color:var(--fb);color:var(--fb)">friendsnet.com/hollowaybus<i style="background:var(--fb)"></i></div>
  <div class="post"><div class="avatar"></div><p>Lorem ipsum dolor sit amet, consectetur adipiscing elit, sed do eiusmod tempor incididunt ut labore et dolore magna aliqua. Ut enim ad minim veniam, quis nostrud exercitation.</p></div>
  <div class="post"><div class="avatar"></div><p>Lorem ipsum dolor sit amet, consectetur adipiscing elit, sed do eiusmod tempor incididunt ut labore et dolore magna aliqua. Ut enim ad minim veniam, quis nostrud exercitation.</p></div>
</div>
<div class="abs feed" style="left:441px;top:1774px">
  <div class="feed-head" style="border-color:var(--tw);color:var(--tw)">chirpline.com/hollowaybus<i style="background:var(--tw)"></i></div>
  <div class="post"><div class="avatar"></div><p>Lorem ipsum dolor sit amet, consectetur adipiscing elit, sed do eiusmod tempor incididunt ut labore et dolore magna aliqua. Ut enim ad minim veniam, quis nostrud exercitation.</p></div>
  <div class="post"><div class="avatar"></div><p>Lorem ipsum dolor sit amet, consectetur adipiscing elit, sed do eiusmod tempor incididunt ut labore et dolore magna aliqua. Ut enim ad minim veniam, quis nostrud exercitation.</p></div>
</div>
<div class="abs feed" style="left:791px;top:1774px">
  <div class="feed-head" style="border-color:var(--gp);color:var(--gp)">circlesnet.com/hollowaybus<i style="background:var(--gp)"></i></div>
  <div class="post"><div class="avatar"></div><p>Lorem ipsum dolor sit amet, consectetur adipiscing elit, sed do eiusmod tempor incididunt ut labore et dolore magna aliqua. Ut enim ad minim veniam, quis nostrud exercitation.</p></div>
  <div class="post"><div class="avatar"></div><p>Lorem ipsum dolor sit amet, consectetur adipiscing elit, sed do eiusmod tempor incididunt ut labore et dolore magna aliqua. Ut enim ad minim veniam, quis nostrud exercitation.</p></div>
</div>

<footer class="abs footer">
  <div class="abs" style="left:91px;top:18px;width:318px;height:176px">
    <h4>Quoting &amp; Booking</h4>
    <div style="display:flex;gap:12px;margin-top:12px">
      <div class="photo" role="img" aria-label="Coach bus" style="width:100px;height:96px;border:3px solid #fff;flex:none"></div>
      <div>
        <div class="display" style="font-size:24px;color:#8d8d8d;line-height:1">Lorem Ipsum</div>
        <p>Lorem ipsum dolor sit amet, consectetur adipiscing elit, sed do eiusmod tempor incididunt ut labore et dolore magna aliqua.</p>
      </div>
    </div>
    <span class="btn" style="position:absolute;right:0;top:146px;height:26px">Get a Quote</span>
  </div>
  <div class="abs" style="left:439px;top:18px;width:316px">
    <h4>Latest Posts</h4>
    <div class="post"><div class="photo" role="img" aria-label="Bus photo" style="width:62px;height:55px;flex:none;border:2px solid #fff"></div><p style="color:var(--footer-text)">Lorem ipsum dolor sit amet, consectetur adipiscing elit, sed do eiusmod tempor incididunt ut labore et dolore magna aliqua. Ut enim ad minim veniam, quis nostrud exercitation.</p></div>
    <div class="post"><div class="photo" role="img" aria-label="Bus photo" style="width:62px;height:55px;flex:none;border:2px solid #fff"></div><p style="color:var(--footer-text)">Lorem ipsum dolor sit amet, consectetur adipiscing elit, sed do eiusmod tempor incididunt ut labore et dolore magna aliqua. Ut enim ad minim veniam, quis nostrud exercitation.</p></div>
  </div>
  <div class="abs" style="left:789px;top:18px;width:320px;height:176px">
    <h4>Join Our VIP Club</h4>
    <p style="margin-top:8px">Lorem ipsum dolor sit amet, consectetur adipiscing elit, sed do eiusmod tempor incididunt ut labore et dolore magna aliqua.</p>
    <div class="field" style="margin-top:8px">Name</div>
    <div class="field" style="margin-top:7px">Email</div>
    <span class="btn" style="position:absolute;right:0;top:148px;height:26px">Join Our VIP Club</span>
  </div>
</footer>

<div class="abs bottom-bar">
  <div class="abs" style="left:91px;top:15px;font-size:11px;color:#777">© 2014 Holloway Bus Company. All Rights Reserved.</div>
  <div class="abs" style="left:952px;top:8px;display:flex;gap:8px;align-items:center">
    <i style="width:28px;height:28px;display:block;background:var(--fb)"></i>
    <i style="width:28px;height:28px;display:block;background:var(--tw)"></i>
    <i style="width:28px;height:28px;display:block;background:var(--gp)"></i>
    <span style="margin-left:14px;font-size:12px;color:var(--blue);text-decoration:underline">Privacy</span>
  </div>
</div>

</body>
</html>
```